Stylish Business Card for Modern hair salon

I need a simple business card design using our salon logo and colours that are in the logo. We service clients of all ages but predominantly those in the 18 to 55 age range. We have a young staff and are looking to have a card that will present a modern and clean image that represents who we are. The card should be in black and white same as our logo. Minimal use of other colours is allowed.

Industry/Entity Type

Hair And Beauty

Contact Information for Business Card

The design should have the following information
salon name - TR Hair Studio
address - 2751 Birchfield Rd.E. Mississauga, ON L7P3K2
phone - 905 614-2870
website - trhairexample.ca
instagram - tr.hairstudio
twitter - @TR_HairStudio

Colors
000000
ffffff
474747

Requirements
Must have
• simple design, salon name, address, phone, website, instagram, twitter info
• Back of card should have the following:
• YOUR NEXT APPOINTMENT
• DATE
• TIME
Nice to have
• simple design, clear to see and read,
• predominantly black and white colour, minimal use of other colours is ok
Should not have
• many colours, various fonts

```html
<!DOCTYPE html>
<html lang="en">
<head>
<meta charset="utf-8">
<title>TR Hair Studio – Business Card</title>
<link rel="stylesheet" href="https://fonts.googleapis.com/css2?family=Electrolize&family=Michroma&display=swap">
<style>
  :root {
    --ink: #000000;
    --paper: #ffffff;
    --slate: #474747;
    --backdrop: #e4e4e4;
    --card-shadow: rgba(0, 0, 0, 0.18);
  }
  html, body {
    margin: 0;
    padding: 0;
    width: 1200px;
    height: 1000px;
    overflow: hidden;
    background: var(--backdrop);
  }
  .sheet {
    width: 1200px;
    height: 1000px;
    display: flex;
    flex-direction: column;
    align-items: center;
    justify-content: center;
    gap: 36px;
  }
  .card {
    width: 760px;
    height: 434px;
    display: block;
    box-shadow: 0 6px 18px var(--card-shadow);
  }
  .brand-name { font-family: "Electrolize", sans-serif; }
  .detail-text {
    font-family: "Michroma", sans-serif;
    font-size: 9.5px;
    letter-spacing: 0.6px;
    fill: var(--paper);
  }
  .label-text {
    font-family: "Michroma", sans-serif;
    fill: var(--paper);
  }
  .dash-line {
    fill: none;
    stroke: var(--paper);
    stroke-width: 1.4;
    stroke-dasharray: 5 3;
  }
  .icon-stroke {
    fill: none;
    stroke: var(--slate);
    stroke-width: 1.8;
  }
</style>
</head>
<body>
<main class="sheet">

  <!-- Front of card -->
  <svg class="card card-front" viewBox="0 0 760 434" xmlns="http://www.w3.org/2000/svg" aria-label="Business card front">
    <rect width="760" height="434" fill="var(--paper)"/>
    <polygon class="front-corner" points="0,0 760,0 760,4 0,194" fill="var(--ink)"/>
    <line class="dash-line" x1="0" y1="178" x2="712" y2="0"/>

    <text class="brand-name logo-name" x="30" y="64" font-size="26" fill="var(--paper)">TR Hair Studio</text>

    <text class="brand-name salon-name" x="62" y="254" font-size="40" fill="var(--ink)">TR Hair Studio</text>

    <!-- phone -->
    <g class="contact-row">
      <rect class="icon-stroke" x="494" y="129" width="11" height="19" rx="2"/>
      <path d="M544,121 H738 V157 H520 Z" fill="var(--slate)"/>
      <path class="dash-line" d="M547,126 H735 M523,152 H735"/>
      <text class="detail-text" x="568" y="143">905 614-2870</text>
    </g>
    <!-- website -->
    <g class="contact-row">
      <circle class="icon-stroke" cx="500" cy="192" r="9"/>
      <path class="icon-stroke" d="M491,192 H509 M500,183 C494,188 494,196 500,201 M500,183 C506,188 506,196 500,201" stroke-width="1.2"/>
      <path d="M544,174 H738 V210 H520 Z" fill="var(--slate)"/>
      <path class="dash-line" d="M547,179 H735 M523,205 H735"/>
      <text class="detail-text" x="568" y="196">TRHAIREXAMPLE.CA</text>
    </g>
    <!-- instagram -->
    <g class="contact-row">
      <circle class="icon-stroke" cx="500" cy="251" r="8"/>
      <path d="M544,233 H738 V269 H520 Z" fill="var(--slate)"/>
      <path class="dash-line" d="M547,238 H735 M523,264 H735"/>
      <text class="detail-text" x="568" y="255">TR.HAIRSTUDIO</text>
    </g>
    <!-- twitter -->
    <g class="contact-row">
      <circle cx="500" cy="308" r="8" fill="var(--slate)"/>
      <path d="M544,290 H738 V326 H520 Z" fill="var(--slate)"/>
      <path class="dash-line" d="M547,295 H735 M523,321 H735"/>
      <text class="detail-text" x="568" y="312">@TR_HairStudio</text>
    </g>
    <!-- address -->
    <g class="contact-row">
      <path class="icon-stroke" d="M140,378 C133,370 133,364 140,360 C147,364 147,370 140,378 Z" stroke-width="1.6"/>
      <circle cx="140" cy="366" r="2" fill="var(--slate)"/>
      <path d="M190,350 H738 V388 H166 Z" fill="var(--slate)"/>
      <path class="dash-line" d="M193,355 H735 M169,383 H735"/>
      <text class="detail-text" x="212" y="373">2751 Birchfield Rd.E. Mississauga, ON L7P3K2</text>
    </g>
  </svg>

  <!-- Back of card -->
  <svg class="card card-back" viewBox="0 0 760 434" xmlns="http://www.w3.org/2000/svg" aria-label="Business card back">
    <rect width="760" height="434" fill="var(--ink)"/>
    <text class="brand-name logo-name" x="380" y="160" font-size="40" text-anchor="middle" fill="var(--paper)">TR Hair Studio</text>

    <rect class="appointment-band" y="290" width="760" height="144" fill="var(--slate)"/>
    <text class="label-text" x="380" y="332" font-size="17" letter-spacing="4" text-anchor="middle">YOUR NEXT APPOINTMENT</text>
    <text class="label-text" x="60" y="392" font-size="11" letter-spacing="2">DATE</text>
    <line x1="120" y1="392" x2="360" y2="392" stroke="var(--paper)" stroke-width="1.2"/>
    <text class="label-text" x="400" y="392" font-size="11" letter-spacing="2">TIME</text>
    <line x1="460" y1="392" x2="700" y2="392" stroke="var(--paper)" stroke-width="1.2"/>
  </svg>

</main>
</body>
</html>
```